New London based construction company website

We need a website designing for our new London based construction company which aims to provide total & fernway yard services.

The website is to have two sides to it one for "halcrest build services" and one for "fernway yard services" with an opening page with both logo's to choose from.

Would like the website to be modern, professional and inspire confidence.

Target Market(s)

Those specifically visiting the site to check that the company is professional

Industry/Entity Type

Construction

Contact Information for Business Card

One side for Fernway Yard Services the other Halcrest Build Services

Number of Pages Required

5+ page

Font styles to use
Sans Serif

Requirements
Must have
• The website is to have two sides to it one for "halcrest build services" and one for "fernway yard services" with an opening page with both logo's to choose from.

```html
<!DOCTYPE html>
<html lang="en">
<head>
<meta charset="utf-8">
<title>Halcrest Build Services &amp; Fernway Yard Services</title>
<link href="https://fonts.googleapis.com/css2?family=Lato:wght@400;700;900&family=Open+Sans:wght@400;600;700&display=swap" rel="stylesheet">
<style>
:root{
  --gold:#e9b11e;
  --ink:#1b1b1d;
  --paper:#ffffff;
  --mist:#eeeeee;
  --body:#6a6a6a;
  --white:#ffffff;
}
*{box-sizing:border-box;margin:0;padding:0}
html,body{width:800px;height:1200px;overflow:hidden;background:var(--mist);font-family:'Open Sans',sans-serif}
.page{position:relative;width:800px;height:1200px;overflow:hidden}
.topbar{position:absolute;left:0;top:0;width:800px;height:34px;background:var(--ink);z-index:3}
.brand{position:absolute;left:100px;top:9px;display:flex;align-items:center;gap:6px;color:var(--white);font-size:6.5px;line-height:7px;font-weight:700;text-transform:uppercase;letter-spacing:.2px}
.brand-mark{width:14px;height:14px;background:#2f6fb3;border-radius:2px}
.nav{position:absolute;left:299px;top:13px;display:flex;gap:11px;font-size:5.6px;font-weight:700;text-transform:uppercase;letter-spacing:-.1px}
.nav a{color:#cfcfcf;text-decoration:none}
.nav a.active{color:var(--white);border-bottom:1px solid var(--white);padding-bottom:1px}
.nav a.gold{color:var(--gold)}
.social{position:absolute;display:flex;gap:5px}
.social span{width:15px;height:15px;border-radius:50%;background:var(--white);display:block}
.topbar .social{left:608px;top:9px}
.hero{position:absolute;left:0;top:34px;width:800px;height:354px;background:linear-gradient(160deg,#6c6a6a 0%,#8c8586 30%,#5b5a5e 60%,#3f4044 100%)}
.hero-title{position:absolute;left:0;top:48px;width:800px;text-align:center;font-family:'Lato',sans-serif;font-weight:900;font-size:41px;color:var(--gold);letter-spacing:.5px}
.hero-sub{position:absolute;left:0;top:96px;width:800px;text-align:center;font-family:'Lato',sans-serif;font-size:16px;line-height:18px;color:var(--white)}
.choice{position:absolute;top:214px;width:180px;text-align:center;color:var(--white)}
.choice.left{left:160px}
.choice.right{left:460px}
.choice-name{font-family:'Open Sans',sans-serif;font-weight:700;font-size:22px;line-height:26px;letter-spacing:.5px;text-transform:uppercase}
.choice-sub{font-size:10px;text-transform:uppercase;margin-top:1px}
.btn{display:inline-block;width:124px;height:30px;line-height:30px;margin-top:14px;border-radius:4px;font-family:'Lato',sans-serif;font-weight:700;font-size:12.5px;letter-spacing:.5px;text-transform:uppercase}
.btn.light{background:var(--white);color:var(--gold)}
.btn.solid{background:var(--gold);color:var(--white)}
.band{position:absolute;left:0;top:388px;width:800px;height:30px;background:var(--gold)}
.panel{position:absolute;background:var(--paper);text-align:center;padding:0 26px}
.panel h2{font-family:'Lato',sans-serif;font-weight:700;font-size:26px;line-height:30px;color:var(--gold);text-transform:uppercase}
.panel p{font-size:6.4px;line-height:12px;color:var(--body);margin-top:12px}
.panel.one{left:100px;top:418px;width:300px;height:287px;padding-top:26px}
.panel.two{left:400px;top:717px;width:300px;height:321px;padding-top:24px}
.photo{position:absolute}
.photo.loader{left:400px;top:418px;width:300px;height:299px;background:linear-gradient(150deg,#3d4a5c 0%,#2a3038 40%,#6d5a22 70%,#2a2520 100%)}
.photo.digger{left:100px;top:705px;width:300px;height:333px;background:linear-gradient(160deg,#7a5a40 0%,#9a5a26 45%,#6f4b34 75%,#5a4231 100%)}
.footer{position:absolute;left:0;top:1038px;width:800px;height:162px;background:linear-gradient(180deg,#2a2a2a 0%,#3a3a3a 55%,#1f1f1f 100%)}
.footer-info{position:absolute;left:100px;top:86px;color:var(--white);font-size:9.5px;line-height:10.8px;font-weight:600}
.footer-info .legal{display:block}
.footer .social{left:608px;top:136px}
</style>
</head>
<body>
<div class="page">
  <header class="topbar">
    <div class="brand"><span class="brand-mark"></span><span>Halcrest &amp; Fernway<br>Site Services</span></div>
    <nav class="nav">
      <a href="#">Home</a>
      <a href="#" class="active">Halcrest Build Services</a>
      <a href="#" class="gold">Fernway Yard Services</a>
      <a href="#" class="gold">Contact</a>
    </nav>
    <div class="social"><span></span><span></span><span></span><span></span><span></span></div>
  </header>

  <section class="hero" role="img" aria-label="Dark workshop scene with timber beams, gears and machinery parts">
    <h1 class="hero-title">HOW CAN WE HELP</h1>
    <p class="hero-sub">We provide complete and professional<br>site solution for your project</p>
    <div class="choice left">
      <div class="choice-name">Halcrest</div>
      <div class="choice-sub">Build Services</div>
      <a class="btn light">Get Started</a>
    </div>
    <div class="choice right">
      <div class="choice-name">Fernway</div>
      <div class="choice-sub">Yard Services</div>
      <a class="btn solid">Get Started</a>
    </div>
  </section>

  <div class="band"></div>

  <article class="panel one">
    <h2>Halcrest Build Services</h2>
    <p>Halcrest offers a complete and professional Client and Candidate Recruitment Service; our Clients are introduced to their own Account Manager who looks after every requirement from Inception of a project to Final Account.</p>
    <p>We adhere to the REC regulations and work to the IRP code of practice. This gives our clients the peace of mind that they are assured of receiving a reputable quality service adhering to a recognised code of practice.</p>
    <p>Our Candidates can expect a first rate agency that will be honest and reliable, always making sure that the Candidate is receiving repeat work and their loyalty is recognised. We require all our Candidates to have CSCS and relevant qualifications or experience within their trade. Most of our candidates are using the CIS scheme but for those who don't we accept PAYE candidates.</p>
    <p>Please provide your own text for this area.</p>
  </article>
  <div class="photo loader" role="img" aria-label="Yellow wheel loader on a site at dusk"></div>

  <div class="photo digger" role="img" aria-label="Orange tracked excavator on sandy ground"></div>
  <article class="panel two">
    <h2>Fernway Yard<br>Services</h2>
    <p>Fernway offers a complete and professional Client and Candidate Recruitment Service; our Clients are introduced to their own Account Manager who looks after every requirement from Inception of a project to Final Account.</p>
    <p>We adhere to the REC regulations and work to the IRP code of practice. This gives our clients the peace of mind that they are assured of receiving a reputable quality service adhering to a recognised code of practice.</p>
    <p>Our Candidates can expect a first rate agency that will be honest and reliable, always making sure that the Candidate is receiving repeat work and their loyalty is recognised. We require all our Candidates to have CSCS and relevant qualifications or experience within their trade. Most of our candidates are using the CIS scheme but for those who don't we accept PAYE candidates.</p>
    <p>Please provide your own text for this area.</p>
  </article>

  <footer class="footer" role="img" aria-label="Dim night view of a London clock tower">
    <div class="footer-info">
      Halcrest Build Services<br>
      48 Corbel Lane, E9 4QT, London<br>
      Get in contact if you have any questions<br>
      Phone: 020 7946 0812<br>
      Email: hello@halcrestbuild.example<br>
      <span class="legal">© 2017 HALCREST BUILD SERVICES. All rights reserved. &nbsp;| &nbsp;Terms of Service</span>
    </div>
    <div class="social"><span></span><span></span><span></span><span></span><span></span></div>
  </footer>
</div>
</body>
</html>
```